Brochure Design Project - Innovative Service for Pharma Industry

Our start up is based in Germany, near Munich and we provide an innovative Service for the pharma industry. We develop product trainings and general trainings online. The adressed audience for these trainings are pharmacies and medics. The parma industry could increase the number of trainings, while saving money (incl a success guarantee). Our (not yet finnished) corporate page can be reviewed here: www.brevoloq.biz, our 'product & service' page is www.kestrumlearn.com. The color code should be leaned towards the corporate page.

The brochure should be send to decision makers in the pharma industry and rise the interest in innovative service. Seriousity should meet modern & clear design.Something eye cathing on the front page might be required.

Target Market(s)

Usually more conservative decision makers within the pharma industry

Industry/Entity Type

Industry

Requirements
Must have
• Conceptional design for an brochure (Din A4 size) of approx 6-8 pages, that capture the key messages (exact content would be filled / provided from us)
Nice to have
• Implementing some of the pics / phrases on the home page www.brevolq.biz could be maybe nice. How about a personal statement from the founder combined with a pic(pic attached)? Both is no must....

```html
<!DOCTYPE html>
<html lang="de">
<head>
<meta charset="utf-8">
<title>brevoloq – Vorteile</title>
<link href="https://fonts.googleapis.com/css2?family=Dosis:wght@300;400;500&display=swap" rel="stylesheet">
<style>
:root{
  --canvas:#e6e6e6;
  --paper:#ffffff;
  --accent:#d9553a;
  --band:#5a5a5a;
  --text:#4a4a4a;
  --logo-grey:#7a7a7a;
  --logo-bg:#f4f4f4;
}
*{margin:0;padding:0;box-sizing:border-box}
html,body{width:1200px;height:3311px;overflow:hidden;background:var(--canvas)}
body{font-family:"Dosis",sans-serif;color:var(--text);position:relative}
.page{position:absolute;left:34px;width:1134px;height:1594px;background:var(--paper);overflow:hidden}
.page--pharmacy{top:34px}
.page--doctors{top:1684px}
.tab{position:absolute;right:0;top:0;width:565px;height:91px;background:var(--accent);color:#fff;font-size:40px;font-weight:400;text-align:center;line-height:91px;letter-spacing:1px}
.footer-band{position:absolute;left:0;right:0;bottom:0;height:58px;background:var(--band)}
.logo-box{position:absolute;left:102px;bottom:0;width:216px;height:173px;background:var(--logo-bg);display:flex;flex-direction:column;align-items:center;justify-content:flex-start;padding-top:18px;gap:8px}
.logo-box .dot{width:62px;height:62px;border-radius:50%;background:var(--logo-grey)}
.logo-box .name{font-size:30px;font-weight:500;color:var(--logo-grey);line-height:34px}
.col{position:absolute;font-size:17.5px;font-weight:400;line-height:18.6px;text-align:justify;letter-spacing:0.1px}
.col--left{left:71px;width:466px;top:243px}
.col--right{left:600px;width:468px;top:222px}
.page--doctors .col--left{top:238px}
.page--doctors .col--right{top:226px}
.col h2{font-size:27px;font-weight:400;color:var(--accent);line-height:30px;margin-bottom:14px}
.col h3{font-size:17px;font-weight:400;color:var(--accent);line-height:18.6px}
.col p{margin-bottom:18px}
</style>
</head>
<body>

<section class="page page--pharmacy">
  <div class="tab">vorteile</div>
  <div class="col col--left">
    <h2>Apotheker</h2>
    <p>Als unabhängiger Dienstleister bietet Kestrumlearn eine Vielzahl verschiedener Vorteile für unterschiedliche Berufsgruppen. Lesen Sie mehr über den Nutzen den unser kostenloser Service Ihnen als Apothekerin oder Apotheker bringt.</p>
    <h3>Großes Schulungsangebot</h3>
    <p>Kestrumlearn dient Ihnen und Ihren Mitarbeitern als zentrale Anlaufstelle für zukünftige Produktschulungen der Pharmaindustrie und ist auch für Sie völlig kostenlos.</p>
    <p>Als industrieabdeckende Plattform bieten wir Ihnen eine hohe Auswahl von Trainings an, um ein umfassendes Maß an Produktwissen sicherzustellen. Das erleichtert Ihnen Ihre Arbeit.</p>
    <p>Die Trainingsinhalte sind so zusammengestellt, dass Sie und Ihre Angestellten mit minimalem Zeitaufwand ein Maximum an Wissen vermittelt bekommen. Optimieren Sie Ihren Zeitaufwand und stellen Sie sicher, dass Ihre Apotheke den besten Dienst am Kunden bieten kann.</p>
    <h3>Bonussystem</h3>
    <p>Wir belohnen Sie und Ihre Angestellten für die Schulungen. Jeder Teilnehmer erhält für die meistens Training bis zu 100 Bonuspunkte*.</p>
    <p>Die gesammelten Bonuspunkte können Sie dann anschließend in unserem Bonusshop in wertvolle Produkte einlösen. Ob und in welcher Höhe Bonuspunkte durch eine Produktschulung erworben werden, wird in den allgemeinen Schulungsinformationen angezeigt.</p>
    <p>Unter allen Teilnehmern führen wir vereinzelte Verlosungen von wertvollen Preisen durch.</p>
    <p>Sie sehen also: Mitmachen lohnt sich für Sie mehrfach.</p>
    <h3>Rabatte</h3>
    <p>Der pharmazeutischen Industrie ist ein hoher Schulungsstand sehr wichtig. Deshalb möchte sie Ihnen zusätzliche Trainingsanreize bieten und unterstützt Sie oder Ihre Einkaufsgemeinschaft ggf. mit zusätzlichen Produktrabatten.</p>
  </div>
  <div class="col col--right">
    <p>teilgenommen hat.</p>
    <p>Ob ein zusätzlicher Rabatt bei einer bestimmten Schulung in Frage kommt, wird Ihnen bei den generellen Informationen der jeweiligen Produktschulung angezeigt.</p>
    <h3>Qualität</h3>
    <p>In Ihrem Beruf tragen Sie ein höchstes Maß an Verantwortung gegenüber Ihrer Kundschaft. Ihre eigene Weiterbildung und die Ihrer Mitarbeiter liegen Ihnen – und uns – sehr am Herzen.</p>
    <p>Kestrumlearn erleichtert Ihnen diese Aufgabe enorm.</p>
    <p>Zum einen durch einen zentralen Zugriff auf Produktschulungen verschiedener Pharmaunternehmen und zum anderen durch eine automatische Zertifizierung bei erfolgreichem Abschluss der Trainings. Das vereinfacht Ihnen die Pflege des Qualitäts-Management-Systems und die Kontrolle Ihrer Angestellten. Selbstverständlich wird hierbei auf die Einhaltung der gültigen Datenschutz-Richtlinien geachtet.</p>
    <h3>Planung</h3>
    <p>Sie entscheiden frei, welches der Ihnen angebotenen Trainings und Schulungen Sie belegen möchten. Daneben haben Sie die volle Flexibilität die Schulungen dann durchzuführen wenn Sie Zeit und Lust haben, z.B. wenn Ihre Apotheke nächtlichen Notdienst hat.</p>
    <p>Eine effiziente Ausrichtung der Trainings mit Blick auf die Vermittlung der wesentlichen Punkte ist selbstverständlich. Im Übrigen entfällt mit Kestrumlearn die Planung von Produktschulungen Ihrer Mitarbeiter durch Pharmareferenten. Urlaube oder krankheitsbedingte Ausfälle von Mitarbeitern stellen somit kein Problem mehr da.</p>
    <h3>Kosten sparen</h3>
    <p>Mit unserer Hilfe haben sich zeitaufwendige Planungen von Produktschulungen mit Pharmareferenten erledigt.</p>
    <p>Keine Überstunden für Trainings nach Feierabend, keine umfassenden Einschränkungen für Ihre Kunden, falls Sie Schulungen bisher auch während der Öffnungszeiten durchgeführt haben.</p>
    <p>Das spart Ihnen Zeit für Planung und Geld für Überstunden.</p>
  </div>
  <div class="footer-band"></div>
  <div class="logo-box"><span class="dot"></span><span class="name">brevoloq</span></div>
</section>

<section class="page page--doctors">
  <div class="tab">vorteile</div>
  <div class="col col--left">
    <h2>Ärzte</h2>
    <h3>Großes Schulungsangebot</h3>
    <p>Auch Ihnen als Arzt und Ihren Mitarbeitern bietet Kestrumlearn eine zentrale Anlaufstelle für zukünftige Produktschulungen der Pharmaindustrie. Und das absolut kostenlos.</p>
    <p>Als größte &amp; unabhängige Online Akademie bieten wir Ihnen regelmäßig eine Vielzahl von Schulungen aus der gesamten Pharmaindustrie und bilden so ein breites Spektrum an Produktwissen ab.</p>
    <p>Die Schulungsinhalte sind mit dem Blick auf das Wesentliche erstellt, sodass Sie und Ihre Mitarbeiter mit kleinstem Zeitaufwand ein Maximum an Wissen vermittelt bekommen.</p>
    <p>Verschwenden Sie keine Zeit mehr und stellen Sie sicher, dass Sie und Ihre Praxismitarbeiter auf dem allerneusten Wissenstand bleiben.</p>
    <h3>Bonussystem</h3>
    <p>Unser Service ist nicht nur kostenlos. Jeder Teilnehmer bekommt für ein erfolgreiches Training bis zu 100 Bonuspunkte*. Die gesammelten Bonuspunkte können Sie anschließend in unserem Bonusshop in wertvolle Geschenke einlösen.</p>
    <p>Des Weiteren führen wir vereinzelte Verlosungen wertvoller Preise unter allen Teilnehmern durch.</p>
    <p>Mitmachen lohnt sich für Sie also vielfach.</p>
    <h3>CME Punkte</h3>
    <p>Jeder Arzt muss kontinuierlich Zeit in seine Weiterbildung investieren. Wir helfen Ihnen dabei auf eine einfache Weise.</p>
    <p>In unserer Academy finden Sie zukünftig Schulungen &amp; Weiterbildungen, die im Vorfeld von der Velmora-Ärztekammer als Fortbildung anerkannt wurden und für die Sie entsprechende Fortbildungspunkte bekommen können.</p>
    <p>Wenn Sie bei der Registrierung Ihre EFN mit angeben, werden von uns Ihre bei uns erworbenen Fortbildungspunkte automatisch durch den EIV weitergeleitet.</p>
  </div>
  <div class="col col--right">
    <p>HINWEIS: Die Verfügbarkeit von CME Schulungen wird für Anfang 2013 erwartet.</p>
    <h3>Qualität</h3>
    <p>In Ihrem Beruf obliegt Ihnen das höchste Maß an Verantwortung gegenüber Ihren Patienten. Ihre eigene Weiterbildung und die Ihrer Mitarbeiter ist oberste Pflicht.</p>
    <p>Kestrumlearn erleichtert Ihnen diese Aufgabe ungemein. Ein zentraler Zugriff auf Produktschulungen verschiedener Pharmaunternehmen und eine automatische Zertifizierung, bei erfolgreichem Abschluss der Trainings, vereinfacht Ihnen (und Ihren Angestellten) die Weiterbildung.</p>
    <h3>Produktmuster</h3>
    <p>Auch bei Kestrumlearn bekommen Sie weiterhin Ihr kostenloses Produktmuster – Vertreterbesuche sind dazu jedoch nicht mehr nötig.</p>
    <p>Sie absolvieren einfach online eine der Schulungen über neue Produkte und unser automatisiertes Reporting teilt den jeweiligen Herstellern mit welcher Arzt erfolgreich daran teilgenommen hat. Daraufhin versenden die Hersteller die Produktmuster direkt an Sie – ganz automatisch*.</p>
    <p>*Voraussetzung hierfür ist die Teilnahme des Pharmaunternehmen an diesem Programm.</p>
    <h3>Planung</h3>
    <p>Sie entscheiden selber, welche der Ihnen angebotenen Schulungen Sie absolvieren möchten. Daneben sind Sie flexibel, die kurzen Trainings dann durchzuführen, wenn Sie Zeit und Lust dazu haben, z.B. wenn Sie nachts wieder einmal Notdienst haben.</p>
    <p>Eine effiziente Ausrichtung der Trainings mit dem Blick auf die wesentliche Punkte ist ein Hauptaugenmerk. Im Übrigen entfällt mit Kestrumlearn die umständliche Planung von Produktschulungen Ihrer Mitarbeiter durch Referenten. Urlaube oder krankheitsbedingte Ausfälle von Mitarbeitern stellen kein Problem mehr dar.</p>
  </div>
  <div class="footer-band"></div>
  <div class="logo-box"><span class="dot"></span><span class="name">brevoloq</span></div>
</section>

</body>
</html>
```